Corvanel Aviation Needs a New Website

1. Details about the company
The website is for a company that conducts businesses in Singapore, Africa and Australia. The name of the Company is Corvanel.
The services include
• Aviation engineering services
• Aviation consulting
• Aviation equipment supplies
• Aviation construction projects
• Aviation business development
2. The designing
• The design can be custom design or premium template redesign
• The theme must be very classy and corporate
• Images to be used on the site must represent the services that the company conducts (5 images)
• The company logo is supplied to be used on the homepage and for the favicon
• The design to be installed on www.corvanel-example.com
3. The Pages
There will be 5 pages.
a. Home
• With latest news widget (showing the 3 latest news)
• Newsfeed, Microblog links
b. About us
c. News
• Weekly news will be posted on this page and the latest news widget will be shown on the homepage
d. Services
• With Request-for-a-quote plugin
e. Contact Us
• Phone numbers
• Fax numbers
• Email addresses
• Google map address plugin for up to 3 locations

```html
<!DOCTYPE html>
<html lang="en">
<head>
<meta charset="utf-8">
<title>Corvanel Aviation</title>
<link rel="stylesheet" href="https://fonts.googleapis.com/css2?family=Anton&family=Arimo:ital@0;1&family=Open+Sans:wght@400;600;700&display=swap">
<style>
:root{
  --ink:#1e1e1e;
  --header:#1f1f1f;
  --footer:#272727;
  --footer-bottom:#232323;
  --accent:#a8161d;
  --text:#333;
  --muted:#555;
  --footer-text:#c9c9c9;
  --rule:#cfcfcf;
  --white:#fff;
}
*{box-sizing:border-box;margin:0;padding:0}
html,body{width:1131px;height:1200px;overflow:hidden;background:var(--white)}
body{position:relative;font-family:"Open Sans",sans-serif;color:var(--text)}
.abs{position:absolute}

/* header */
.site-header{left:0;top:0;width:1131px;height:66px;background:var(--header)}
.brand{left:94px;top:14px;display:flex;align-items:center;gap:8px;font-family:"Open Sans",sans-serif;font-weight:700;font-size:27px;color:#cfcfcf;letter-spacing:.3px}
.brand-dot{width:10px;height:10px;border-radius:50%;background:#cfcfcf}
.main-nav{right:95px;top:26px;display:flex;gap:49px}
.main-nav a{color:var(--white);font-size:10.5px;text-decoration:none;letter-spacing:.2px}

/* hero */
.hero{left:0;top:66px;width:1131px;height:478px;
  background:linear-gradient(180deg,#5a5140 0%,#b08a3a 30%,#e9a92a 55%,#d9781a 68%,#4a3a2a 78%,#8a7a66 100%)}
.hero-title{left:700px;top:125px;font-family:"Anton",sans-serif;line-height:1}
.hero-title .l1{display:block;font-size:47px;color:#1c1c1c;letter-spacing:.5px}
.hero-title .l2{display:block;font-size:36px;color:var(--accent);margin-top:1px}
.slide-arrow{top:292px;width:30px;height:30px;border-radius:50%;background:rgba(255,255,255,.25)}
.slide-arrow.prev{left:33px}.slide-arrow.next{left:1052px}

/* services */
.service{width:183px;top:482px}
.service-frame{width:183px;height:128px;background:var(--white);padding:8px}
.service-photo{width:166px;height:107px}
.service-name{margin-top:12px;padding-left:9px;font-size:10.5px;color:#222}
.service-link{margin-top:6px;padding-left:9px;font-size:10.5px;color:var(--accent);display:flex;align-items:center;gap:5px}

/* news */
.section-title{left:93px;top:697px;font-size:14.5px;font-weight:700;color:#222}
.news-nav{left:1007px;top:704px;display:flex;gap:3px}
.news-rule{left:93px;top:730px;width:945px;height:1px;background:var(--rule)}
.news-photo{top:757px;width:176px;height:120px}
.news-body{top:757px;width:250px}
.news-head{font-size:9.5px;font-weight:700;color:#222;line-height:18px;text-transform:uppercase}
.news-date{font-size:10.5px;color:var(--accent);margin-top:5px}
.news-text{font-size:10.5px;color:var(--muted);line-height:21px;margin-top:3px}

/* footer */
.site-footer{left:0;top:929px;width:1131px;height:223px;background:var(--footer);font-family:"Arimo",sans-serif}
.footer-bottom{left:0;top:1152px;width:1131px;height:48px;background:var(--footer-bottom);
  text-align:center;line-height:48px;font-size:9.5px;color:#aaa;font-family:"Open Sans",sans-serif}
.col-title{font-family:"Open Sans",sans-serif;font-size:12px;color:var(--white);letter-spacing:.2px}
.quote{font-style:italic;font-size:9.5px;color:var(--footer-text);line-height:18.5px;width:205px}
.footer-links a{display:block;color:var(--footer-text);font-size:9.5px;text-decoration:none;line-height:21px}
.contact-line{font-size:9.5px;color:var(--footer-text);line-height:21px;display:flex;align-items:center;gap:8px}
.social{display:flex;align-items:center;gap:6px;font-size:9.5px;color:var(--footer-text)}
.social-icon{width:26px;height:26px;border-radius:50%;background:#9a9a9a}
.footer-brand{left:858px;top:154px;font-family:"Open Sans",sans-serif;font-weight:700;font-size:19px;color:var(--white)}
</style>
</head>
<body>

<header class="site-header abs">
  <div class="brand abs"><span class="brand-dot"></span>Corvanel</div>
  <nav class="main-nav abs">
    <a href="#">HOME</a><a href="#">ABOUT US</a><a href="#">NEWS</a><a href="#">SERVICES</a><a href="#">CONTACT US</a>
  </nav>
</header>

<section class="hero abs" role="img" aria-label="Passenger jet on an airport apron at sunset under golden clouds"></section>
<h1 class="hero-title abs"><span class="l1">AVIATION</span><span class="l2">ENGINEERING SERVICES</span></h1>
<div class="slide-arrow prev abs"></div>
<div class="slide-arrow next abs"></div>

<div class="service abs" style="left:93px">
  <div class="service-frame"><div class="service-photo" role="img" aria-label="Aircraft nose with ground crew at dusk" style="background:linear-gradient(180deg,#5b6f8e,#c7a26a 60%,#3c3a36)"></div></div>
  <div class="service-name">ENGINEERING SERVICES</div>
  <div class="service-link">Click here for view details <svg width="9" height="9" viewBox="0 0 10 10"><circle cx="5" cy="5" r="5" fill="#a8161d"/><path d="M4 2.8 6.2 5 4 7.2" stroke="#fff" stroke-width="1.4" fill="none"/></svg></div>
</div>
<div class="service abs" style="left:284px">
  <div class="service-frame"><div class="service-photo" role="img" aria-label="Two engineers in hard hats beside an aircraft" style="background:linear-gradient(180deg,#9fb0c0,#8a8a8a 50%,#2c3550)"></div></div>
  <div class="service-name">CONSULTING</div>
  <div class="service-link">Click here for view details <svg width="9" height="9" viewBox="0 0 10 10"><circle cx="5" cy="5" r="5" fill="#a8161d"/><path d="M4 2.8 6.2 5 4 7.2" stroke="#fff" stroke-width="1.4" fill="none"/></svg></div>
</div>
<div class="service abs" style="left:475px">
  <div class="service-frame"><div class="service-photo" role="img" aria-label="Wrench resting on an engine block" style="background:linear-gradient(135deg,#2a2a2a,#6d6d6d 50%,#1c1c1c)"></div></div>
  <div class="service-name">EQUIPMENT SUPPLIES</div>
  <div class="service-link">Click here for view details <svg width="9" height="9" viewBox="0 0 10 10"><circle cx="5" cy="5" r="5" fill="#a8161d"/><path d="M4 2.8 6.2 5 4 7.2" stroke="#fff" stroke-width="1.4" fill="none"/></svg></div>
</div>
<div class="service abs" style="left:665px">
  <div class="service-frame"><div class="service-photo" role="img" aria-label="Jet engine under maintenance in a hangar" style="background:linear-gradient(180deg,#d6d9dc,#9a9ea2 60%,#6b6a62)"></div></div>
  <div class="service-name">CONSTRUCTION PROJECTS</div>
  <div class="service-link">Click here for view details <svg width="9" height="9" viewBox="0 0 10 10"><circle cx="5" cy="5" r="5" fill="#a8161d"/><path d="M4 2.8 6.2 5 4 7.2" stroke="#fff" stroke-width="1.4" fill="none"/></svg></div>
</div>
<div class="service abs" style="left:856px">
  <div class="service-frame"><div class="service-photo" role="img" aria-label="Technicians working at a control panel in a hangar" style="background:linear-gradient(180deg,#c9ccd2,#6b7280 55%,#2f3a5a)"></div></div>
  <div class="service-name">BUSINESS DEVELOPMENT</div>
  <div class="service-link">Click here for view details <svg width="9" height="9" viewBox="0 0 10 10"><circle cx="5" cy="5" r="5" fill="#a8161d"/><path d="M4 2.8 6.2 5 4 7.2" stroke="#fff" stroke-width="1.4" fill="none"/></svg></div>
</div>

<h2 class="section-title abs">LATEST NEWS</h2>
<div class="news-nav abs">
  <svg width="11" height="11" viewBox="0 0 10 10"><circle cx="5" cy="5" r="5" fill="#bbb"/><path d="M6 2.8 3.8 5 6 7.2" stroke="#fff" stroke-width="1.4" fill="none"/></svg>
  <svg width="11" height="11" viewBox="0 0 10 10"><circle cx="5" cy="5" r="5" fill="#bbb"/><path d="M4 2.8 6.2 5 4 7.2" stroke="#fff" stroke-width="1.4" fill="none"/></svg>
</div>
<div class="news-rule abs"></div>

<div class="news-photo abs" style="left:93px" role="img" aria-label="Aircraft silhouette against a sunset sky" style="background:#333"></div>
<div class="news-photo abs" style="left:93px;background:linear-gradient(180deg,#5a5a6a,#c88a40 45%,#2a1c22 70%,#140f18)" role="img" aria-label="Aircraft silhouette against a sunset sky"></div>
<article class="news-body abs" style="left:292px">
  <h3 class="news-head">Es simplemente el texto de relleno<br>de las imprentas</h3>
  <div class="news-date">Posted on 27 January 2015</div>
  <p class="news-text">Es simplemente el texto de relleno de las impren-tas y archivos de texto. Lorem Ipsum ha sido el texto de relleno estándar...</p>
</article>

<div class="news-photo abs" style="left:590px;background:linear-gradient(180deg,#1f4f9a,#6e93c8 45%,#e6ecf2 75%,#9fb6d4)" role="img" aria-label="Airliner flying above white clouds"></div>
<article class="news-body abs" style="left:789px">
  <h3 class="news-head">Es simplemente el texto de relleno<br>de las imprentas</h3>
  <div class="news-date">Posted on 27 January 2015</div>
  <p class="news-text">Es simplemente el texto de relleno de las impren-tas y archivos de texto. Lorem Ipsum ha sido el texto de relleno estándar...</p>
</article>

<footer class="site-footer abs">
  <div class="abs" style="left:139px;top:40px;width:200px;display:flex;justify-content:space-between;align-items:center">
    <span class="col-title">TESTIMONIALS</span>
    <svg width="20" height="8" viewBox="0 0 20 8"><path d="M4 1 1 4l3 3M16 1l3 3-3 3" stroke="#bbb" stroke-width="1.2" fill="none"/></svg>
  </div>
  <p class="quote abs" style="left:138px;top:64px">Lorem Ipsum is simply dummy text of the printing and typesetting industry. Lorem Ipsum has been the industry's standard dummy text ever since</p>
  <div class="abs" role="img" aria-label="Portrait photo of the reviewer" style="left:138px;top:146px;width:40px;height:40px;border-radius:50%;background:#b89a88;border:2px solid #eee"></div>
  <div class="abs" style="left:198px;top:152px;font-size:10px;color:#fff">MARCUS ELDEN</div>
  <div class="abs" style="left:198px;top:170px;font-size:9.5px;font-style:italic;color:var(--footer-text)">Marketing Manager</div>

  <div class="col-title abs" style="left:430px;top:40px">WELCOME</div>
  <nav class="footer-links abs" style="left:431px;top:60px">
    <a href="#">Home</a><a href="#">About us</a><a href="#">News</a><a href="#">Services</a><a href="#">Contact Us</a>
  </nav>

  <div class="col-title abs" style="left:600px;top:40px">CONTACT INFO</div>
  <div class="abs" style="left:600px;top:74px;font-size:10.5px;color:#fff">CORVANEL</div>
  <div class="abs" style="left:601px;top:94px">
    <div class="contact-line">120 Streat Name, State name,</div>
    <div class="contact-line">Country name, Zip code : 2350 3652.</div>
  </div>
  <div class="abs" style="left:602px;top:140px">
    <div class="contact-line"><svg width="9" height="12" viewBox="0 0 9 12"><rect x="1" y=".5" width="7" height="11" rx="1" stroke="#bbb" fill="none"/><circle cx="4.5" cy="9.5" r=".7" fill="#bbb"/></svg>Phone : ( 4410 ) 318 207</div>
    <div class="contact-line" style="margin-top:3px"><svg width="12" height="9" viewBox="0 0 12 9"><rect x=".5" y=".5" width="11" height="8" fill="#bbb"/><path d="M.5 .5 6 5l5.5-4.5" stroke="#272727" fill="none"/></svg>info@corvanel-example.com</div>
  </div>

  <div class="col-title abs" style="left:858px;top:40px">FOLLOW US</div>
  <div class="social abs" style="left:862px;top:65px"><span class="social-icon"></span>: Newsfeed</div>
  <div class="social abs" style="left:862px;top:104px"><span class="social-icon"></span>: Microblog.</div>
  <div class="footer-brand abs">Corvanel</div>
</footer>
<div class="footer-bottom abs">©2015. Corvanel. All rights reserved.</div>

</body>
</html>
```